Visitenkarten-Design für Ferienhausvermietung
Zielgruppe
Vermietung eines Ferienhauses
Aufgabenstellung
Die Visitenkarte sollte edel und hochwertig wirken...
Es wäre mir wichtig, dass die Visitenkarte im Querformat erstellt wird.
Die Farben vom Logo lauten:
green: C = 43 M = 0 Y = 100 N = 16
brown: C = 39 M = 57 J = 87 N = 53
sky blue: C = 14 M = 6 J = 6 N = 0
Aber bitte nicht so viel in den Visitenkarten verwenden. Die Visitenkarten sollen eher neutral gehalten werden.
Die Schriften
font
Lindeneck : Satisfaction
Ferienhaus : Corbert Regular
Flyer-Design für Ferienhausvermietung Flyer-Design für Ferienhausvermietung"
Es soll ein Flyer im Format DIN A4 erstellt werden. Der beidseitig bedruckt wird und dann 6seitig gefaltet wird. Ich benötige für den Flyer: Beschreibung/Ausstattung des Ferienhauses Beschreibung der Lage Beschreibung der Umgebung Anfahrt/Lage/Kontakt
Logo-Design für Ferienhaus ´Sa Morta´auf Mallorca mit eigenem Tennisplatz und Pool Logo-Design für Ferienhaus ´Sa Morta´auf Mallorca mit eigenem Tennisplatz und Pool"
Sie können sich meine Finca auf der Website: Casitorvent anschauen. Ort: Costitx Name des Hauses: Finca Reblat (heißt nur auf der Website so). Der Name am Tor Haus: Finca Sa Morta. Ich mag es gerne klassisch
Logo-Design für ein Feriendorf an der Ostsee Logo-Design für ein Feriendorf an der Ostsee"
* Nicht zu bunt, nicht zu verspielt, möglichst klar und aufgeräumt * In 2D, keine Schattierungen, keine Fotos im Hintergrund o. ä.. * Das Logo muss in allen Medien gut darstellbar sein! * Es sollte modern wirken, dennoch fröhlich, warm und einladend * Der Strand-/Wasserbezug muss deutlich we..
Flyer-Design für Ferienhaus Flyer-Design für Ferienhaus"
Flyerdesign für Ferienhaus: Din-Lang 2x gefalzt (übliche Format), 3 Seiten vorne und hinten.  Es sollte nach Möglichkeit an unsere Webseite (www.ferienhaus-kormoran-tidewik.de) angepasst werden, druckfertig sein und per PDF auf unserer Webseite zum Downloaden integriert werden können. Meh..
Logo-Design für Ferienhaus Logo-Design für Ferienhaus"
Wir suchen ein Moderenes Design gern berücksichtig in Kombination mit dem Naturpark Velmtaler Höhen. Da das Ferienhaus sich dort befindet.

```html
<!DOCTYPE html>
<html lang="de">
<head>
<meta charset="utf-8">
<title>Lindeneck Ferienhaus – Visitenkarte</title>
<link href="https://fonts.googleapis.com/css2?family=Quicksand:wght@500;600&display=swap" rel="stylesheet">
<style>
  :root {
    --backdrop: #2b2e33;
    --sky: #dce6e4;
    --paper: #ffffff;
    --brown: #3e2a20;
    --ink: #2a3550;
    --green: #5aa844;
    --label-bg: #ffffff;
  }
  * { box-sizing: border-box; margin: 0; padding: 0; }
  html, body { width: 1200px; height: 900px; overflow: hidden; }
  body {
    background: var(--backdrop);
    font-family: "Quicksand", sans-serif;
    position: relative;
  }
  .card {
    position: absolute;
    left: 313px;
    width: 574px;
    height: 328px;
    background: var(--paper);
    overflow: hidden;
    box-shadow: 0 2px 6px rgba(0,0,0,.35);
  }
  .card--front { top: 96px; }
  .card--back { top: 476px; }
  .sky-band {
    position: absolute;
    left: 0; top: 0; width: 100%;
    background: var(--sky);
  }
  .card--front .sky-band { height: 244px; }
  .card--back .sky-band { height: 190px; }

  .brand-name {
    position: absolute;
    left: 0; width: 100%;
    text-align: center;
    color: var(--brown);
    font-weight: 600;
    letter-spacing: 1px;
    line-height: 1;
    white-space: nowrap;
  }
  .card--front .brand-name { top: 50px; font-size: 40px; }

  .house-scene {
    position: absolute;
    border-radius: 50%;
    border: 5px solid var(--brown);
    box-shadow: 0 0 0 6px var(--paper);
  }
  .front-scene-clip {
    position: absolute;
    left: 197px; top: 108px;
    width: 180px; height: 136px;
    overflow: hidden;
  }
  .front-scene-clip .house-scene {
    left: 6px; top: 6px; width: 168px; height: 168px;
    background: radial-gradient(circle at 50% 35%, #e3ecea 0%, #cfdcd7 45%, #9fc08a 75%, #6f5444 100%);
  }
  .address-label {
    position: absolute;
    left: 165px; top: 232px;
    width: 243px; height: 22px;
    background: var(--label-bg);
    color: var(--ink);
    font-size: 14.5px;
    font-weight: 500;
    text-align: center;
    line-height: 22px;
  }
  .contact-line {
    position: absolute;
    left: 0; width: 100%;
    color: var(--ink);
    font-size: 15px;
    font-weight: 500;
    display: flex;
    justify-content: center;
    gap: 16px;
    align-items: center;
  }
  .contact-line--phone { top: 270px; }
  .contact-line--web { top: 295px; }
  .contact-item { display: flex; align-items: center; gap: 7px; }
  .icon { width: 13px; height: 13px; fill: var(--green); }

  .back-logo {
    position: absolute;
    left: 175px; top: 48px;
    width: 224px; height: 224px;
    border-radius: 50%;
    background: var(--paper);
  }
  .back-logo .house-scene {
    left: 12px; top: 12px; width: 200px; height: 200px;
    background: linear-gradient(180deg, #dfe8e6 0%, #cfdcd7 30%, #a9c895 52%, #8a6a58 60%, #ffffff 61%, #ffffff 100%);
  }
  .back-logo .brand-name {
    top: 140px;
    font-size: 26px;
  }
</style>
</head>
<body>

<section class="card card--front">
  <div class="sky-band"></div>
  <h1 class="brand-name">Lindeneck</h1>
  <div class="front-scene-clip">
    <div class="house-scene" role="img" aria-label="Illustration des Ferienhauses mit Bäumen im runden Rahmen"></div>
  </div>
  <p class="address-label">Tannweg 12, 91638 Erlbachtal</p>
  <p class="contact-line contact-line--phone">
    <span class="contact-item">
      <svg class="icon" viewBox="0 0 24 24" aria-hidden="true"><path d="M6.6 10.8a15.1 15.1 0 0 0 6.6 6.6l2.2-2.2c.3-.3.7-.4 1-.2 1.1.4 2.3.6 3.6.6.6 0 1 .4 1 1V20c0 .6-.4 1-1 1A17 17 0 0 1 3 4c0-.6.4-1 1-1h3.5c.6 0 1 .4 1 1 0 1.3.2 2.5.6 3.6.1.3 0 .7-.2 1z"/></svg>
      09812/4471052
    </span>
  </p>
  <p class="contact-line contact-line--web">
    <span class="contact-item">
      <svg class="icon" viewBox="0 0 24 24" aria-hidden="true"><path d="M2 5h20v14H2z"/><path d="M3 6l9 6.3L21 6" fill="none" stroke="#fff" stroke-width="1.6"/></svg>
      info@lindeneck-ferienhaus.de
    </span>
    <span class="contact-item">
      <svg class="icon" viewBox="0 0 24 24" aria-hidden="true"><circle cx="12" cy="12" r="10"/><path d="M2 12h20M12 2c3 3 3 17 0 20M12 2c-3 3-3 17 0 20" fill="none" stroke="#fff" stroke-width="1.4"/></svg>
      www.lindeneck-ferienhaus.de
    </span>
  </p>
</section>

<section class="card card--back">
  <div class="sky-band"></div>
  <div class="back-logo">
    <div class="house-scene" role="img" aria-label="Illustration des Ferienhauses mit Bäumen im runden Rahmen"></div>
    <h2 class="brand-name">Lindeneck</h2>
  </div>
</section>

</body>
</html>
```